DAF - EXPO

We are a sport event orgnizer managing diffrent sport events. We would like to orgnize the kick off event of the season Dunlore Athletic Fairs expo will be the gathering point of all sports events happening in Kuwait.
The expected events like Marathons, Forgelift , Triathlons , Karting , Inline skates , BMX.

Target Market(s)
Target market are outdoor and sports enthusiast
Industry/Entity Type
Events
Requirements
Must have
- Name of the event Dunlore Athletic Fairs EXPO
Dates 4-5 October 2013
Location Harbel Quayfront
Instegram account and twitter Zelvoracedays
website www.tarn-wicklo.com.kw
Logos of the events who will participate attached
Nice to have
- Facts:
10 Events
8 Sports
6 Locations
5000+ Participants
in 5 Months ( in big bold so it can be the highlight )

```html
<!DOCTYPE html>
<html lang="en">
<head>
<meta charset="utf-8">
<title>Dunlore Athletic Fairs Expo</title>
<link rel="stylesheet" href="https://fonts.googleapis.com/css2?family=Oswald:wght@400;500;700&family=Satisfy&display=swap">
<style>
  :root {
    --lime: #a9f25a;
    --lime-deep: #8fe03e;
    --ink: #0d0d0d;
    --white: #ffffff;
    --sky-edge: #27478a;
    --sky-mid: #5d95c2;
    --sky-core: #dfe3e6;
    --tile: #4a83b0;
    --brand-grey: #555b60;
  }
  * { margin: 0; padding: 0; box-sizing: border-box; }
  html, body { width: 900px; height: 1200px; overflow: hidden; }
  body { font-family: "Oswald", "Arial Narrow", sans-serif; }
  .poster {
    position: relative; width: 900px; height: 1200px; overflow: hidden;
    background: radial-gradient(ellipse 75% 62% at 50% 58%, var(--sky-core) 0%, #c3ccd3 30%, var(--sky-mid) 62%, var(--sky-edge) 100%);
  }
  .website {
    position: absolute; top: 66px; left: 0; width: 900px; text-align: center;
    color: var(--white); font-weight: 700; font-size: 29px; letter-spacing: 6px;
  }
  .frame { position: absolute; top: 0; left: 0; }
  .title {
    position: absolute; top: 158px; left: 100px; width: 700px; text-align: center;
    color: var(--lime); font-weight: 500; font-size: 80px; line-height: 118px;
    letter-spacing: 2px; text-transform: uppercase; white-space: nowrap;
  }
  .dates {
    position: absolute; top: 408px; left: 0; width: 900px; text-align: center;
    color: var(--ink); font-weight: 700; font-size: 50px; letter-spacing: 5px;
  }
  .venue {
    position: absolute; top: 494px; left: 0; width: 900px; text-align: center;
    font-family: "Satisfy", cursive; font-weight: 400; font-size: 46px; color: var(--ink);
  }
  .venue .at { color: var(--lime-deep); font-size: 30px; vertical-align: 18px; margin-right: 4px; }
  .facts {
    position: absolute; top: 588px; left: 0; width: 900px; text-align: center; list-style: none;
    color: var(--ink); font-weight: 500; font-size: 40px; line-height: 61px; letter-spacing: 4px;
  }
  .highlight {
    position: absolute; top: 852px; left: 232px; width: 448px; height: 92px;
    background: var(--lime); transform: rotate(-2.5deg);
    display: flex; align-items: center; justify-content: center;
    color: var(--ink); font-weight: 700; font-size: 64px; letter-spacing: 4px;
    box-shadow: 0 3px 8px rgba(0,0,0,0.25);
  }
  .social {
    position: absolute; top: 998px; left: 108px; display: flex; gap: 16px; align-items: center; list-style: none;
  }
  .social li { display: flex; align-items: center; gap: 10px; color: var(--ink); font-size: 20px; letter-spacing: 1px; }
  .social .tile { width: 56px; height: 56px; border-radius: 10px; background: var(--tile); }
  .partners {
    position: absolute; top: 1076px; left: 0; width: 900px; height: 124px; background: var(--white);
    display: flex; align-items: center; justify-content: space-around; padding: 0 30px; list-style: none;
  }
  .partners li { display: flex; align-items: center; gap: 8px; color: var(--brand-grey); font-weight: 500; font-size: 21px; }
  .partners .mark { width: 34px; height: 34px; background: var(--brand-grey); }
</style>
</head>
<body>
<main class="poster">
  <p class="website">www.tarn-wicklo.com.kw</p>

  <svg class="frame" width="900" height="1200" viewBox="0 0 900 1200" aria-hidden="true">
    <path d="M190 432 H80 V133 H820 V432 H712" fill="none" stroke="#1a1a1a" stroke-width="2" stroke-dasharray="3 3"/>
  </svg>

  <h1 class="title">Dunlore Athletic<br>Fairs Expo</h1>
  <p class="dates">4-5 October 2013</p>
  <p class="venue"><span class="at">at</span>Harbel Quayfront</p>

  <ul class="facts">
    <li>10 Events</li>
    <li>8 Sports</li>
    <li>6 Locations</li>
    <li>5000+ Participants</li>
  </ul>

  <div class="highlight">IN 5 MONTHS</div>

  <ul class="social">
    <li><span class="tile"></span>Zelvoracedays</li>
    <li><span class="tile"></span>Zelvoracedays</li>
    <li><span class="tile"></span>Dunlore Athletic Fairs</li>
  </ul>

  <ul class="partners">
    <li><span class="mark"></span>Ovrenta</li>
    <li>Stridevo</li>
    <li>Kestral Karting</li>
    <li><span class="mark"></span>Northwold Gear</li>
    <li>Clash Eastmoor</li>
  </ul>
</main>
</body>
</html>
```